Pilates Classes Flyer Design

I need a flyer designed that will promote my range of classes held in Bath, UK. I teach beginners, intermediate level and Over 50's and 60's and also teach individuals in their own homes. I would like to see designs using my colours blue Pantone 306 and Lime Green 14-0452 TPX TCX. The flyer should reflect a friendly, welcoming and professional class structure. I attach an old flyer for your reference and copy.

Target Market(s)

Men and Women who have busy lives working hard, who recognise they need to stretch out, do some exercise and de-stress after a busy day

Ladies over 50 who want to do some Pilates in a friendly fun environment and meet people at the same time.

Industry/Entity Type

It Professional

Font styles to use
Sans Serif
Script

Requirements
Must have
• One-sided flyer
Text only logo. Drop the figure

```html
<!DOCTYPE html>
<html lang="en">
<head>
<meta charset="utf-8">
<title>FlowLine Pilates – New Classes Flyer</title>
<link href="https://fonts.googleapis.com/css2?family=Lato:wght@300;400;700;900&display=swap" rel="stylesheet">
<style>
  :root{
    --cyan:#17b4e6;
    --cyan-deep:#0d7eae;
    --lime:#8dc63f;
    --lime-soft:#c5e38a;
    --navy:#1d3550;
    --white:#ffffff;
    --paper:#f4f6f7;
    --photo-warm:#c9a48e;
    --photo-cool:#8fb8cf;
    --badge:#167f94;
  }
  *{margin:0;padding:0;box-sizing:border-box}
  html,body{width:990px;height:1200px;overflow:hidden;background:var(--white)}
  .flyer{position:relative;width:990px;height:1200px;font-family:'Lato',sans-serif;overflow:hidden;background:linear-gradient(170deg,var(--white) 0%,var(--paper) 100%)}
  .flyer-shapes{position:absolute;inset:0}
  .brand{position:absolute;left:60px;top:75px;width:500px;text-align:center;color:var(--cyan);font-weight:300;font-size:62px;letter-spacing:-1px;line-height:1}
  .headline{position:absolute;left:40px;top:222px;width:540px;text-align:center;font-size:46px;line-height:1.15;color:var(--lime);font-weight:400}
  .headline strong{color:var(--cyan);font-weight:700}
  .headline .dash{display:inline-block;width:34px;height:3px;background:var(--lime);vertical-align:middle;margin:0 20px}
  .intro{position:absolute;left:40px;top:368px;width:540px;text-align:center;font-size:25px;line-height:1.4;color:var(--cyan);font-weight:300}
  .intro em{font-style:normal;color:var(--lime);font-weight:400}
  .benefits{position:absolute;left:70px;top:528px;width:490px;list-style:none}
  .benefit{position:relative;padding-left:80px;margin-bottom:30px}
  .benefit svg{position:absolute;left:0;top:22px;width:56px;height:48px}
  .benefit h3{font-size:23px;font-weight:400;color:var(--cyan);line-height:1.2}
  .benefit p{font-size:18px;font-weight:300;color:var(--cyan);line-height:1.3;margin-top:8px}
  .venues{position:absolute;left:0;top:835px;width:990px;text-align:center;color:var(--white)}
  .venues h2{font-size:30px;line-height:36px;font-weight:700;letter-spacing:.5px;margin-bottom:26px}
  .venue{margin-bottom:14px}
  .venue h4{font-size:20px;line-height:24px;font-weight:700;color:var(--navy);letter-spacing:.3px}
  .venue p{font-size:16px;line-height:20px;font-weight:400}
  .contact{position:absolute;left:0;top:1103px;width:990px;height:97px;display:flex;align-items:center;justify-content:center;color:var(--white)}
  .contact svg{width:76px;height:56px;margin-right:20px}
  .call span{display:block;font-size:24px;font-weight:300;letter-spacing:.5px;line-height:1}
  .call strong{display:block;font-size:34px;font-weight:700;line-height:1.1}
  .divider{width:3px;height:62px;background:var(--white);margin:0 28px}
  .email{font-size:28px;font-weight:400}
</style>
</head>
<body>
<main class="flyer">
  <svg class="flyer-shapes" viewBox="0 0 990 1200" width="990" height="1200">
    <path class="lime-edge" d="M560 0 H605 C612 300 628 580 648 850 L622 855 C598 580 578 300 560 0 Z" fill="var(--lime)"/>
    <path class="photo-top" role="img" aria-label="Photo of smiling women exercising in a pilates class" d="M598 0 H990 V430 H615 C608 300 602 150 598 0 Z" fill="var(--photo-warm)"/>
    <path class="photo-bottom" role="img" aria-label="Photo of a woman stretching sideways with a class behind her" d="M617 446 H990 V790 C880 810 760 830 645 848 C636 700 625 570 617 446 Z" fill="var(--photo-cool)"/>
    <rect class="cert-badge" role="img" aria-label="Certified teacher badge" x="690" y="395" width="250" height="88" rx="10" fill="var(--badge)" stroke="var(--white)" stroke-width="4"/>
    <path class="lime-wave" d="M0 812 C320 848 700 822 990 772 V798 C700 845 320 868 0 838 Z" fill="var(--lime-soft)"/>
    <path class="blue-band" d="M0 836 C320 866 700 843 990 796 V1200 H0 Z" fill="var(--cyan)"/>
    <rect class="footer-rule" x="0" y="1094" width="990" height="6" fill="var(--lime)"/>
    <rect class="footer-band" x="0" y="1100" width="990" height="100" fill="var(--cyan-deep)"/>
  </svg>

  <div class="brand">FlowLine Pilates</div>

  <h1 class="headline"><span class="dash"></span>NEW <strong>CLASSES</strong><span class="dash"></span><br>NEAR YOU!</h1>

  <p class="intro">Pilates is for <em>EVERYONE</em><br>whatever level of fitness, age or ability<br>to help you build strength,<br>flexibility and overall well-being.</p>

  <ul class="benefits">
    <li class="benefit">
      <svg viewBox="0 0 56 48"><path d="M2 26 L12 18 L22 32 L48 2 L54 8 L22 46 Z" fill="var(--lime)"/></svg>
      <h3>Quality teaching with Balance Form Method Teacher.</h3>
      <p>Progressive approach.<br>Teaching good movement skills.</p>
    </li>
    <li class="benefit">
      <svg viewBox="0 0 56 48"><path d="M2 26 L12 18 L22 32 L48 2 L54 8 L22 46 Z" fill="var(--lime)"/></svg>
      <h3>Small class sizes and friendly atmosphere.</h3>
      <p>Beginners, Intermediate and<br>Over 50's classes to choose from.</p>
    </li>
  </ul>

  <section class="venues">
    <h2>JOIN MY ONE-HOUR CLASSES AT</h2>
    <div class="venue"><h4>ST ANNE'S CHURCH HALL, ELM RISE</h4><p>Monday evenings, Tuesday and Friday mornings.</p></div>
    <div class="venue"><h4>WILLOW MEADOWS DR. SURGERY</h4><p>Tuesday evenings.</p></div>
    <div class="venue"><h4>ASHCROFT CENTRE, HILL ROAD,</h4><p>Wednesday mornings and evenings.</p></div>
  </section>

  <footer class="contact">
    <svg viewBox="0 0 76 56" aria-hidden="true">
      <path d="M4 18 C4 6 72 6 72 18 L72 22 L56 22 L54 14 C46 11 30 11 22 14 L20 22 L4 22 Z" fill="var(--white)"/>
      <path d="M22 24 H54 L64 50 H12 Z" fill="var(--white)"/>
      <circle cx="38" cy="37" r="8" fill="var(--cyan-deep)"/>
    </svg>
    <div class="call"><span>CALL CLARA ON</span><strong>07900123456</strong></div>
    <div class="divider"></div>
    <div class="email">clara.hartley@example.co.uk</div>
  </footer>
</main>
</body>
</html>
```